NEW Website DESIGN for Brightwell Panes & Stoneworks Company

Brand New website, contemporary, clean, visual (images), not busy. ATTACHED IS OUR LOG THAT YOU MUST USE.

The company is called Brightwell Panes & Stoneworks (BrightwellPS)
www.brightwellps.com
The website should be www.brightwellpns.com
one page for glass one page for solid surfaces www.brightwellpanesplashes.co.uk
www.brightwellstoneworkss.co.uk

Target Market(s)

Hotels, Commercial projects, Small focus on residential

Industry/Entity Type

Construction

Number of Pages Required

5+ page

Font styles to use
Sans Serif

Requirements
Must have
• COLOURS AS PER OUR LOGO - WHITE/YELLOW/GREY - WHITE BACK GROUND
• CLEAR SIMPLE NAVIGATION - MODER CLEAN CUT - DESIGN FEEL
• LATEST NAVIGATION FOR IMAGES and text to include per project details
• WORK/PROJECT AREA - NEWS AREA - TEAM AREA/ABOUT US/CONTACT US
• NEW PAGEwww.brightwellpanesplashes.co.uk - NEW PAGE www.brightwellstoneworkss.co.uk
• PLEASE COPY THIS TYPE OF TEMPALTE
• https://www.harlowmead.co.uk/project/grand-halls/
• MOBILE READY
• WORDPRESS
• MODERN IMAGES INCLUDING VELMARA KESTRIN AND GLASS PROJECTS
Nice to have
• NEW DESIGN MODER FRESH
• WEBSITES I LIKE THE TEMPLATE SHOULD BE LIKE THE WEBSITE BELOW
• https://www.harlowmead.co.uk/
Should not have
• NOT Old fashion template, not busy NAVIGATION
• NO BLACK
• NO DARK GREYS
• NOT LOTS OF YELLOW
• RESDENTIAL IMAGES

```html
<!DOCTYPE html>
<html lang="en">
<head>
<meta charset="utf-8">
<title>Brightwell Panes &amp; Stoneworks</title>
<link rel="stylesheet" href="https://fonts.googleapis.com/css2?family=Arimo:wght@400;500&display=swap">
<style>
  :root {
    --ink: #1c1c1c;
    --ink-soft: #555555;
    --body-grey: #8a8a8a;
    --nav-active: #5a5a4a;
    --accent-teal: #3ecfa4;
    --button-fill: #c4c4c4;
    --header-light: #f6f6f6;
    --header-dark: #d4d4d4;
    --band-light: #f7f7f7;
    --band-dark: #c6c6c6;
    --footer-light: #b9b9b9;
    --footer-dark: #a2a2a2;
    --bar: #c9c9c9;
    --thumb: #f2f6f4;
  }
  * { box-sizing: border-box; margin: 0; padding: 0; }
  html, body { width: 960px; height: 1200px; overflow: hidden; }
  body {
    position: relative;
    font-family: "Arimo", Arial, sans-serif;
    color: var(--ink);
    letter-spacing: -0.4px;
    background: #ffffff;
  }
  a { color: inherit; text-decoration: none; }

  /* Header */
  .site-header {
    position: absolute; left: 0; top: 0; width: 960px; height: 78px;
    background: linear-gradient(90deg, var(--header-light), var(--header-dark));
  }
  .brand { position: absolute; left: 104px; top: 18px; display: flex; align-items: center; gap: 8px; }
  .brand-mark { width: 22px; height: 22px; border-radius: 50%; background: #e3e034; }
  .brand-name { font-size: 13px; color: var(--ink-soft); font-weight: 500; line-height: 1.2; width: 120px; }
  .main-nav { position: absolute; left: 441px; top: 34px; display: flex; gap: 18px; font-size: 17px; }
  .main-nav .is-current { color: var(--nav-active); }
  .search-icon { position: absolute; left: 822px; top: 31px; }

  /* Hero */
  .hero {
    position: absolute; left: 0; top: 78px; width: 960px; height: 372px;
    background: linear-gradient(90deg, var(--band-light), var(--band-dark));
  }
  .hero-title { position: absolute; left: 109px; top: 136px; font-size: 24px; font-weight: 400; }
  .hero-lead { position: absolute; left: 106px; top: 174px; width: 320px; font-size: 19px; line-height: 23px; color: var(--ink-soft); }
  .btn {
    position: absolute; display: flex; align-items: center; justify-content: center;
    background: var(--button-fill); border: 1px solid var(--accent-teal); border-right-color: #aaa; border-bottom-color: #999;
    box-shadow: 2px 2px 3px rgba(0,0,0,0.25); font-size: 13px; color: var(--ink);
  }
  .hero .btn { left: 104px; top: 256px; width: 95px; height: 35px; }
  .gallery-title { position: absolute; left: 438px; width: 418px; top: 25px; text-align: center; font-size: 19px; font-weight: 400; }
  .gallery-slide {
    position: absolute; left: 438px; top: 62px; width: 418px; height: 242px;
    background: linear-gradient(180deg, #f1f2f4 0%, #e4e4e8 28%, #c52a63 42%, #b01f52 60%, #f3f3f3 68%, #c9b8a2 100%);
  }
  .slide-arrow { position: absolute; top: 168px; }
  .slide-arrow.prev { left: 443px; }
  .slide-arrow.next { left: 815px; }
  .slide-dots { position: absolute; left: 632px; top: 334px; display: flex; gap: 2px; }
  .slide-dots span { width: 6px; height: 6px; border-radius: 50%; background: #6a6a6a; }
  .slide-dots span.active { background: #2a2a2a; }

  /* Products */
  .products {
    position: absolute; left: 0; top: 450px; width: 960px; height: 527px;
    background: linear-gradient(90deg, var(--band-light), var(--band-dark));
  }
  .section-title { position: absolute; left: 0; width: 960px; top: 43px; text-align: center; font-size: 19px; font-weight: 400; }
  .product { position: absolute; top: 76px; width: 178px; }
  .product-photo { width: 176px; height: 158px; }
  .product-name { margin-top: 20px; font-size: 19px; line-height: 23px; font-weight: 400; }
  .product-text { margin-top: 8px; font-size: 14px; line-height: 17.4px; color: var(--body-grey); }
  .p1 { left: 104px; } .p1 .product-photo { background: linear-gradient(160deg, #4a4f55, #e8e8ea 60%, #3c3f44); }
  .p2 { left: 296px; } .p2 .product-photo { background: linear-gradient(170deg, #f2efe6, #c8b58c 50%, #8fd6c8 65%, #f0f0f0); }
  .p3 { left: 488px; } .p3 .product-photo { background: linear-gradient(180deg, #f4f4f4, #e4e4e4 60%, #4a2e24 85%, #e9e9e9); }
  .p4 { left: 681px; } .p4 .product-photo { background: linear-gradient(90deg, #f1f1f1, #8a8784 45%, #6e6b67 70%, #d8d8d8); }
  .p1 .product-text { margin-left: -2px; }
  .p2 .product-name { margin-left: -1px; }
  .p2 .product-text { margin-left: 1px; }
  .p3 .product-name { margin-left: 3px; }
  .p4 .product-name { margin-left: 2px; }

  /* Footer */
  .site-footer {
    position: absolute; left: 0; top: 977px; width: 960px; height: 189px;
    background: linear-gradient(90deg, var(--footer-light), var(--footer-dark));
  }
  .trade-note { position: absolute; left: 106px; top: 30px; width: 230px; font-size: 14px; line-height: 18px; }
  .site-footer .btn { left: 104px; top: 83px; width: 78px; height: 30px; font-size: 12px; }
  .footer-heading { position: absolute; top: 28px; font-size: 15px; font-weight: 400; }
  .contact-heading { left: 362px; }
  .news-heading { left: 618px; top: 30px; }
  .contact-line { position: absolute; left: 360px; font-size: 14px; line-height: 14px; }
  .news-item { position: absolute; left: 616px; display: flex; gap: 8px; width: 250px; }
  .news-thumb { width: 48px; height: 41px; background: var(--thumb); flex: none; }
  .news-text { font-size: 11px; line-height: 13.4px; }

  /* Bottom bar */
  .bottom-bar { position: absolute; left: 0; top: 1166px; width: 960px; height: 34px; background: var(--bar); }
  .copyright { position: absolute; left: 104px; top: 10px; font-size: 14px; }
  .social { position: absolute; left: 426px; top: 8px; display: flex; gap: 12px; }
  .social span { width: 18px; height: 18px; border-radius: 50%; background: #2a2a2a; }
  .legal-nav { position: absolute; left: 621px; top: 9px; display: flex; gap: 18px; font-size: 14px; }
</style>
</head>
<body>

<header class="site-header">
  <a class="brand" href="#">
    <span class="brand-mark"></span>
    <span class="brand-name">Brightwell Panes &amp; Stoneworks</span>
  </a>
  <nav class="main-nav">
    <a class="is-current" href="#">Home</a>
    <a href="#">What we do</a>
    <a href="#">Products</a>
    <a href="#">News</a>
    <a href="#">Contacts</a>
  </nav>
  <svg class="search-icon" width="26" height="28" viewBox="0 0 26 28" aria-label="Search">
    <circle cx="15" cy="11" r="8" fill="none" stroke="#1c1c1c" stroke-width="2"/>
    <line x1="9.5" y1="17" x2="3" y2="25" stroke="#1c1c1c" stroke-width="2.2" stroke-linecap="round"/>
  </svg>
</header>

<section class="hero">
  <h1 class="hero-title">Welcome !</h1>
  <p class="hero-lead">A leading manufacturer of glass and Velmara products for trade professionals and residential clients.</p>
  <a class="btn" href="#">Get a quote</a>

  <h2 class="gallery-title">Gallery</h2>
  <div class="gallery-slide" role="img" aria-label="Kitchen with magenta glass splashback, white worktop and extractor hood"></div>
  <svg class="slide-arrow prev" width="34" height="34" viewBox="0 0 34 34" aria-label="Previous slide">
    <circle cx="17" cy="17" r="16" fill="rgba(255,255,255,0.25)" stroke="#444" stroke-width="1.5"/>
    <path d="M21 9 L11 17 L21 25 Z" fill="#666"/>
  </svg>
  <svg class="slide-arrow next" width="34" height="34" viewBox="0 0 34 34" aria-label="Next slide">
    <circle cx="17" cy="17" r="16" fill="rgba(255,255,255,0.25)" stroke="#444" stroke-width="1.5"/>
    <path d="M13 9 L23 17 L13 25 Z" fill="#666"/>
  </svg>
  <div class="slide-dots"><span></span><span class="active"></span><span></span><span></span></div>
</section>

<section class="products">
  <h2 class="section-title">Products</h2>

  <article class="product p1">
    <div class="product-photo" role="img" aria-label="Bathroom with white solid-surface vanity and dark tiled wall"></div>
    <h3 class="product-name">Bespoke Velmara</h3>
    <p class="product-text">Kestrin™ Velmara® is becoming the worksurface of choice among trade professionals, customer-facing businesses and home-owners in the know. It is versatile, resilient, lightweight, durable, bonda­ble, water-resistant and avail­able in a variety of sizes, which can be cut to shape easily.  Perfect for kitchens, bathrooms, lobbies and bars</p>
  </article>

  <article class="product p2">
    <div class="product-photo" role="img" aria-label="Kitchen with aqua glass worktop and white cabinets"></div>
    <h3 class="product-name">Contemporary Glass, Worktops and Splash backs</h3>
    <p class="product-text">A bespoke glass worktop or splashback, from Brightwell Pane Splashes, creates a distinctive designer style in any room be it in a home, business or commercial pro­ject. Crisp and clean, availa­ble in any colour, a glass worktop or splashback can really add the wow factor.</p>
  </article>

  <article class="product p3">
    <div class="product-photo" role="img" aria-label="Bathroom with large mirror above white basins on dark wood unit"></div>
    <h3 class="product-name">Beautiful Mirrors</h3>
    <p class="product-text">Manufactured in house we have a vast range of mirror frames to suit all styles from modern to contemporary. Bathrooms mirrors are turned around quickly (1 -3 days de­pending the specification), from a simply cut and pol­ished or beveled mirror to LED and Heated Mirrors.</p>
  </article>

  <article class="product p4">
    <div class="product-photo" role="img" aria-label="Wet room with grey stone walls and frameless glass shower screen"></div>
    <h3 class="product-name">Wet Rooms</h3>
    <p class="product-text">Because everything is manu­factured in house, we can create glass shower enclo­sures for any size of bath­room or wet room. Made be­spoke for your project, our 10mm thick, toughened glass is available in an excellent selection of colours with the option to add images!</p>
  </article>
</section>

<footer class="site-footer">
  <p class="trade-note">All our bespoke products available for trade professionals</p>
  <a class="btn" href="#">Get Quote</a>

  <h2 class="footer-heading contact-heading">CONTACT US</h2>
  <p class="contact-line" style="top:64px">+44 (0)1632 960 418</p>
  <p class="contact-line" style="top:91px">sales@brightwellpanesplash<br>es.co.uk</p>

  <h2 class="footer-heading news-heading">NEWS</h2>
  <div class="news-item" style="top:63px">
    <div class="news-thumb"></div>
    <p class="news-text">Lorem ipsum dolor sit amet, consectetur adipisicing elit, sed do eiusmod tempor incididunt ut labore et dolore magna al</p>
  </div>
  <div class="news-item" style="top:112px">
    <div class="news-thumb"></div>
    <p class="news-text">Lorem ipsum dolor sit amet, consectetur adipisicing elit, sed do eiusmod tempor incididunt ut labore et dolore magna al</p>
  </div>
</footer>

<div class="bottom-bar">
  <p class="copyright">CopyRight 2018 All Rights Reserved</p>
  <div class="social" aria-label="Social links"><span></span><span></span><span></span></div>
  <nav class="legal-nav">
    <a href="#">Home</a>
    <a href="#">Terms</a>
    <a href="#">Privacy Policy</a>
  </nav>
</div>

</body>
</html>
```